Surface Protection company needs cards

We are a New Zealand company that will apply nanotechnology coatings on surfaces to prevent growth and spread of bacteria, viruses, mold etc with a sprayer. We deal with large corporates, airlines, hospitals and schools so we are after a new modern, simple and clean look that will have great visual impact.
We a company that is focused on prevention and protection.

Company name, Vela Shield

Subtext, Antimicrobial Surface Protection

Logo, VS

Target Market(s)

Hospitals, Transport agencies, Airlines, Corporate entities

Contact Information for Business Card

Company name, VelaShield
Logo, VS

Gareth Tolley
velashieldnz@postbox.example
+64219305562
www.velashield.example.nz

Requirements
Must have
• Simple clean look.
Nice to have
• We apply nano coatings so try and incorporate this into a theme somehow

```html
<!DOCTYPE html>
<html lang="en">
<head>
<meta charset="utf-8">
<title>Vela Shield – Business Card</title>
<link rel="stylesheet" href="https://fonts.googleapis.com/css2?family=Josefin+Sans:wght@300;400;600&family=Oswald:wght@500&display=swap">
<style>
  :root {
    --page: #e9e9ea;
    --card: #f2f2f2;
    --ink-grey: #6b6b70;
    --blue-deep: #2a67b1;
    --blue-light: #45b3d9;
    --white: #ffffff;
  }
  * { box-sizing: border-box; margin: 0; padding: 0; }
  html, body { width: 1200px; height: 1200px; overflow: hidden; }
  body {
    background: var(--page);
    font-family: "Josefin Sans", sans-serif;
    position: relative;
  }
  .card {
    position: absolute;
    left: 227px;
    width: 746px;
    height: 425px;
    box-shadow: 0 14px 28px rgba(0,0,0,0.18);
  }
  .card--front { top: 135px; background: var(--card); }
  .card--back {
    top: 639px;
    background: linear-gradient(90deg, var(--blue-light) 0%, #3a9acb 45%, var(--blue-deep) 100%);
    overflow: hidden;
  }

  /* front */
  .brand {
    position: absolute;
    left: 40px;
    top: 52px;
    display: flex;
    align-items: center;
    gap: 22px;
  }
  .brand__dot {
    width: 72px; height: 72px;
    border-radius: 50%;
    border: 3px solid var(--blue-light);
  }
  .brand__name {
    font-family: "Oswald", sans-serif;
    font-weight: 500;
    font-size: 52px;
    line-height: 1;
    color: var(--ink-grey);
    letter-spacing: -0.5px;
  }
  .brand__tagline {
    font-size: 17px;
    font-weight: 400;
    color: var(--ink-grey);
    letter-spacing: 1.6px;
    margin-top: 10px;
  }
  .holder {
    position: absolute;
    left: 38px;
    top: 262px;
    font-size: 25px;
    font-weight: 600;
    letter-spacing: 1px;
  }
  .holder__first { color: var(--blue-deep); }
  .holder__last { color: var(--blue-light); }
  .divider {
    position: absolute;
    left: 0; right: 0;
    top: 314px;
    height: 1.5px;
    background: linear-gradient(90deg, var(--blue-light), var(--blue-deep));
  }
  .contacts {
    position: absolute;
    left: 38px;
    top: 344px;
    list-style: none;
    font-size: 18px;
    font-weight: 300;
    color: var(--ink-grey);
  }
  .contacts li { display: flex; align-items: center; gap: 9px; height: 25px; }
  .contacts svg { width: 17px; height: 17px; flex: none; }
  .website {
    position: absolute;
    right: 36px;
    top: 372px;
    font-size: 16px;
    font-weight: 300;
    color: var(--ink-grey);
    letter-spacing: 0.5px;
  }
  .website strong { font-weight: 600; color: var(--blue-deep); }

  /* back */
  .card__texture {
    position: absolute; inset: 0;
    background: linear-gradient(90deg, rgba(255,255,255,0.05), rgba(255,255,255,0.02));
  }
  .back-brand {
    position: absolute;
    inset: 0;
    display: flex;
    flex-direction: column;
    align-items: center;
    justify-content: center;
    color: var(--white);
  }
  .back-brand__dot {
    width: 110px; height: 110px;
    border-radius: 50%;
    border: 3px solid var(--white);
    margin-bottom: 24px;
  }
  .back-brand__name {
    font-family: "Oswald", sans-serif;
    font-weight: 500;
    font-size: 64px;
    line-height: 1;
  }
  .back-brand__tagline {
    font-size: 20px;
    letter-spacing: 2px;
    margin-top: 12px;
  }
</style>
</head>
<body>
  <section class="card card--front">
    <div class="brand">
      <div class="brand__dot"></div>
      <div>
        <div class="brand__name">Vela Shield</div>
        <div class="brand__tagline">Antimicrobial Surface Protection</div>
      </div>
    </div>

    <p class="holder"><span class="holder__first">GARETH</span> <span class="holder__last">TOLLEY</span></p>
    <div class="divider"></div>

    <ul class="contacts">
      <li>
        <svg viewBox="0 0 20 20" aria-hidden="true"><circle cx="10" cy="10" r="10" fill="#2a67b1"/><path d="M5 8.5c0-1.5 2.5-2.5 5-2.5s5 1 5 2.5l-1.8 0.6-0.6-1.4h-5.2l-0.6 1.4zM6.5 14l1.2-4h4.6l1.2 4z" fill="#fff"/><circle cx="10" cy="11.8" r="1.1" fill="#2a67b1"/></svg>
        +64219305562
      </li>
      <li>
        <svg viewBox="0 0 20 20" aria-hidden="true"><circle cx="10" cy="10" r="10" fill="#45b3d9"/><rect x="5" y="6.5" width="10" height="7" fill="none" stroke="#fff" stroke-width="1"/><path d="M5 6.5l5 4 5-4M5 13.5l3.5-3.5M15 13.5l-3.5-3.5" fill="none" stroke="#fff" stroke-width="1"/></svg>
        velashieldnz@postbox.example
      </li>
    </ul>

    <p class="website">www.<strong>velashield</strong>.example.nz</p>
  </section>

  <section class="card card--back">
    <div class="card__texture" role="img" aria-label="Faint repeating molecule pattern across the blue gradient"></div>
    <div class="back-brand">
      <div class="back-brand__dot"></div>
      <div class="back-brand__name">Vela Shield</div>
      <div class="back-brand__tagline">Antimicrobial Surface Protection</div>
    </div>
  </section>
</body>
</html>
```